Halcyon Skyways Global Business Card

I would like a professional business card designed. The plane that is being used is a Vortan Aero Ridgeline 740. Our primary business colors would be navy blue and light blue. This is a charter plane for hire. Our clients range from business people to vacation goers. A website is currently under development and two of the primary pictures being used will be attached. The pictures don't need to be used in the business card design, but could be used for inspiration and reference. We will need our P.O. Box address on the card and personal information (Name, cell number, email address, and website address (www.halcyonskywaysglobal.example)) Thanks! God Bless!
Updates

The contact info for the back of the card: Milo Dearborn Cell: 555.014.2738 Email: mdearborn@halcyonskywaysglobal.example

Target Market(s)

Business people

Industry/Entity Type

Business

Contact Information for Business Card

This will be on a standard square cornered business card.

Requirements
Must have
• Professional look

```html
<!DOCTYPE html>
<html lang="en">
<head>
<meta charset="utf-8">
<title>Halcyon Skyways Global Business Card</title>
<link href="https://fonts.googleapis.com/css2?family=Lato:wght@300;400;700&display=swap" rel="stylesheet">
<style>
  :root {
    --backdrop: #1b1d1e;
    --brand-blue: #1a4bff;
    --accent-orange: #f7700f;
    --ink-dark: #3b4045;
    --ink-black: #141618;
    --card-light: #ffffff;
    --card-grey: #dcdee0;
    --white: #ffffff;
  }
  * { margin: 0; padding: 0; box-sizing: border-box; }
  html, body {
    width: 1200px; height: 864px; overflow: hidden;
    background: var(--backdrop);
    font-family: "Lato", Arial, sans-serif;
  }
  .stage { position: relative; width: 1200px; height: 864px; }
  .card {
    position: absolute; left: 352px; width: 526px; height: 309px;
    box-shadow: 0 4px 12px rgba(0,0,0,0.45);
    overflow: hidden;
  }
  .card-front {
    top: 96px;
    background: linear-gradient(180deg, var(--card-light) 0%, var(--card-grey) 100%);
  }
  .card-back { top: 445px; height: 310px; background: var(--brand-blue); }

  .brand { position: absolute; display: flex; align-items: center; }
  .brand-dot { border-radius: 50%; flex: none; }
  .brand-name { font-weight: 300; line-height: 1; text-transform: uppercase; }
  .brand-name span { display: block; }

  .card-front .brand { left: 30px; top: 116px; gap: 12px; }
  .card-front .brand-dot { width: 38px; height: 38px; background: var(--accent-orange); }
  .card-front .brand-name { color: var(--brand-blue); font-size: 20px; letter-spacing: 1px; }
  .card-front .brand-name span + span { margin-top: 4px; }
  .card-front .brand-name .brand-sub { font-size: 9px; letter-spacing: 3px; }

  .contact {
    position: absolute; left: 222px; top: 80px; right: 14px;
    color: var(--ink-dark); white-space: nowrap;
  }
  .contact-name { font-size: 22px; font-weight: 700; line-height: 1.1; }
  .contact-role { font-size: 15px; color: var(--ink-black); margin-top: 2px; }
  .contact-list { list-style: none; margin-top: 24px; font-size: 14px; line-height: 22px; }
  .contact-list b { font-weight: 400; color: var(--ink-black); }

  .address-band {
    position: absolute; left: 0; bottom: 0; width: 100%; height: 48px;
    background: var(--brand-blue); color: var(--white);
    font-size: 15px; display: flex; align-items: center; justify-content: center;
    padding-left: 24px;
  }

  .card-back .brand { left: 135px; top: 125px; gap: 28px; }
  .card-back .brand-dot { width: 68px; height: 68px; background: var(--white); }
  .card-back .brand-name { color: var(--white); font-size: 34px; letter-spacing: 1.5px; }
  .card-back .brand-name span + span { margin-top: 10px; }
  .card-back .brand-name .brand-sub { font-size: 15px; letter-spacing: 6px; }
</style>
</head>
<body>
<main class="stage">
  <section class="card card-front">
    <div class="brand">
      <div class="brand-dot"></div>
      <p class="brand-name"><span>Halcyon</span><span>Skyways</span><span class="brand-sub">Global</span></p>
    </div>
    <div class="contact">
      <h1 class="contact-name">Milo Dearborn</h1>
      <p class="contact-role">Managing Director</p>
      <ul class="contact-list">
        <li><b>T:</b> 555.014.2738</li>
        <li><b>E:</b> mdearborn@halcyonskywaysglobal.example</li>
        <li><b>W:</b> www.halcyonskywaysglobal.example</li>
      </ul>
    </div>
    <div class="address-band">P.O. Box 4127, Larkspur Field, Country, 908145</div>
  </section>

  <section class="card card-back">
    <div class="brand">
      <div class="brand-dot"></div>
      <p class="brand-name"><span>Halcyon</span><span>Skyways</span><span class="brand-sub">Global</span></p>
    </div>
  </section>
</main>
</body>
</html>
```